Vantor surface design based website for technology jobs website

We need a website design for a technology job listing website, mainly aiming at 20/30/40 year old nerds. Jobs listed from multiple sources will be concatenated and organised. This website will be built with Vantor surface design (https://plexiform.example/guidelines/) so please use their components. The design should be simple and clear, so a user can directly look for offerings that are interesting for him.

Three different pages will be needed:

1. Main jobs list page

Contains a large table (https://plexiform.example/guidelines/components/data-tables.html#data-tables-structure), on top or next to this data-table users should be able to apply filters (select countries, select salary ranges) and somewhere an overview of the selected filters should be shown.

- A subscribe bar should be shown somewhere to allow a user to register for weekly/monthly mailings for new job offers with his preferred search filters.

2. Selected item page

If an item is clicked, a user should be able to view a job posting and it's details.

3. An advertiser should be able post his job offer.
Similar fields as https://submit.quarrowlisting.example/.
(https://plexiform.example/guidelines/components/text-fields.html#text-fields-layout)

Target Market(s)

20/30/40 year old nerds.

Industry/Entity Type

Computer

Logo Text

TalonWork.example

Number of Pages Required

3 page

Colors

Designer to choose colors to be used in the design.

Requirements
Must have
• 1. Main jobs list page
• Contains a large table (https://plexiform.example/guidelines/components/data-tables.html#data-tables-structure), on top or next to this data-table users should be able to apply filters (select countries, select salary ranges) and somewhere an overview of the selected filters should be shown.
• - A subscribe bar should be shown somewhere to allow a user to register for weekly/monthly mailings for new job offers with his preferred search filters.
• 2. Selected item page
• If an item is clicked, a user should be able to view a job posting and it's details.
• 3. An advertiser should be able post his job offer,
• (https://plexiform.example/guidelines/components/text-fields.html#text-fields-layout)
• Please use open fonts!

```html
<!DOCTYPE html>
<html lang="en">
<head>
<meta charset="utf-8">
<title>Veldmark – Job Listings</title>
<link href="https://fonts.googleapis.com/css2?family=Montserrat:wght@400;500;600;700&family=Open+Sans:ital,wght@0,400;0,600;1,400&display=swap" rel="stylesheet">
<style>
:root{
  --blue:#1a7fd4;
  --blue-dark:#1366b0;
  --orange:#e8431f;
  --page:#e6e6e8;
  --white:#ffffff;
  --ink:#1d1d1f;
  --muted:#555;
  --head:#4a4a4a;
  --line:#cfcfd2;
  --panel:#d5d5d8;
}
*{box-sizing:border-box;margin:0;padding:0}
html,body{width:714px;height:1200px;overflow:hidden}
body{position:relative;background:var(--page);font-family:"Open Sans",Arial,sans-serif;color:var(--ink)}
.abs{position:absolute}

/* header */
.site-header{position:absolute;left:0;top:0;width:714px;height:39px;background:var(--white)}
.brand{position:absolute;left:78px;top:8px;font-family:"Montserrat",Arial,sans-serif;font-weight:500;font-size:18px;color:var(--blue);letter-spacing:.2px}
.nav a{position:absolute;top:13px;height:14px;line-height:14px;font-family:"Montserrat",Arial,sans-serif;font-size:6.4px;font-weight:500;color:var(--ink);text-decoration:none;letter-spacing:.2px}
.nav a.active{background:var(--orange);color:var(--white);padding:0 6px}
.post-job{position:absolute;left:571px;top:10px;width:65px;height:19px;background:var(--blue);color:var(--white);font-family:"Montserrat",Arial,sans-serif;font-weight:700;font-size:7.6px;line-height:19px;text-align:center;letter-spacing:.3px}

/* hero */
.hero{position:absolute;left:0;top:39px;width:714px;height:207px;background:linear-gradient(180deg,#1e7fd6 0%,#2a8ae0 55%,#1f79cc 100%)}
.hero-welcome{position:absolute;left:0;width:714px;top:46px;text-align:center;font-family:"Montserrat",Arial,sans-serif;color:var(--white);font-size:12.5px;letter-spacing:.3px}
.hero-title{position:absolute;left:0;width:714px;top:58px;text-align:center;font-family:"Montserrat",Arial,sans-serif;color:var(--white);font-weight:500;font-size:30px}
.search{position:absolute;left:146px;top:117px;width:444px;height:28px;background:var(--white);border:2px solid #c9d3dc}
.search span{position:absolute;top:0;line-height:24px;font-family:"Montserrat",Arial,sans-serif;font-size:7px;color:#333}
.search .divider{position:absolute;left:240px;top:0;width:1px;height:24px;background:#c9c9c9}
.search-btn{position:absolute;right:2px;top:1px;width:59px;height:22px;background:var(--orange);color:var(--white);font-family:"Montserrat",Arial,sans-serif;font-weight:700;font-size:8.6px;line-height:22px;text-align:center;letter-spacing:.4px}

/* listing */
.section-title{position:absolute;left:78px;top:268px;font-family:"Montserrat",Arial,sans-serif;font-weight:600;font-size:10.5px;letter-spacing:.2px}
.select{position:absolute;top:265px;height:21px;background:var(--white);border:1px solid #c8c8cb;font-size:6.8px;line-height:19px;padding-left:8px;color:#333}
.select svg{position:absolute;right:8px;top:7px}

.jobs{position:absolute;left:78px;top:298px;width:559px;background:var(--white)}
.jobs-head,.job{display:grid;grid-template-columns:240px 102px 68px 68px 81px}
.jobs-head{height:20px;background:var(--head);color:var(--white);font-family:"Montserrat",Arial,sans-serif;font-size:6.2px;font-weight:500;line-height:20px;letter-spacing:.2px}
.jobs-head div{text-align:center;border-right:1px solid #666}
.jobs-head div:first-child{text-align:left;padding-left:15px}
.jobs-head div:last-child{border-right:none}
.job{height:53.7px;border-bottom:1px solid #e4e4e6}
.job:last-child{border-bottom:none}
.job > div{border-right:1px solid var(--line);padding-top:14px;font-size:7px;text-align:center}
.job > div:first-child{text-align:left;padding-left:17px}
.job > div:last-child{border-right:none}
.job-title{font-family:"Montserrat",Arial,sans-serif;font-weight:600;font-size:7.6px;color:var(--ink);margin-bottom:2px}
.job-company{font-size:6.2px;color:#333;margin-bottom:3px}
.job-posted{font-size:6.2px;font-style:italic;color:#444}
.apply{display:inline-block;margin-top:5px;width:50px;height:14px;background:var(--blue);color:var(--white);font-family:"Montserrat",Arial,sans-serif;font-weight:700;font-size:5.6px;line-height:14px;letter-spacing:.4px}

.pager{position:absolute;left:542px;top:871px;display:flex;gap:4px}
.pager span{width:10px;height:10px;border:1px solid #9a9a9a;background:var(--white);font-size:5.6px;line-height:8px;text-align:center}
.pager span.arrow{background:var(--blue);border-color:var(--blue)}

/* newsletter */
.newsletter{position:absolute;left:78px;top:923px;width:559px;height:90px;background:var(--panel);border:1px solid #b9b9bc}
.newsletter h2{position:absolute;left:23px;top:22px;font-family:"Montserrat",Arial,sans-serif;font-size:8.6px;font-weight:600;text-decoration:underline;letter-spacing:.2px}
.field{position:absolute;top:52px;width:123px;height:15px;border-bottom:2px solid var(--white);font-size:7px;color:#222}
.signup{position:absolute;left:472px;top:42px;width:69px;height:26px;background:var(--orange);color:var(--white);font-family:"Montserrat",Arial,sans-serif;font-weight:700;font-size:8.6px;line-height:26px;text-align:center;letter-spacing:.4px}

/* footer */
.site-footer{position:absolute;left:0;top:1043px;width:714px;height:157px;background:var(--blue);color:var(--white)}
.foot-col{position:absolute;top:27px}
.foot-col h3{font-family:"Montserrat",Arial,sans-serif;font-weight:700;font-size:7px;letter-spacing:.4px;margin-bottom:10px}
.foot-col a{display:block;font-size:6.3px;line-height:10.4px;color:var(--white);text-decoration:none}
.foot-col.social a{padding-left:11px;position:relative}
.foot-col.social a::before{content:"";position:absolute;left:0;top:2.6px;width:5px;height:5px;border-radius:50%;background:var(--white)}
.foot-brand{position:absolute;left:531px;top:29px;font-family:"Montserrat",Arial,sans-serif;font-weight:500;font-size:22px}
.copyright{position:absolute;left:531px;top:63px;font-size:5.6px}
</style>
</head>
<body>

<header class="site-header">
  <div class="brand">Veldmark</div>
  <nav class="nav">
    <a class="active" style="left:298px">HOME</a>
    <a style="left:346px">ABOUT US</a>
    <a style="left:403px">JOB LISTING</a>
    <a style="left:462px">SERVICES</a>
    <a style="left:513px">CONTACT US</a>
  </nav>
  <div class="post-job">POST A JOB</div>
</header>

<section class="hero" role="img" aria-label="Blue-tinted aerial photo of a city skyline at dusk">
  <div class="hero-welcome">WELCOME TO</div>
  <div class="hero-title">Veldmark</div>
  <div class="search">
    <span style="left:12px">Job Title Keywords</span>
    <div class="divider"></div>
    <span style="left:252px">Location</span>
    <div class="search-btn">SEARCH</div>
  </div>
</section>

<h1 class="section-title">JOB LISTINGS</h1>
<div class="select" style="left:454px;width:88px">Select Countries
  <svg width="6" height="4" viewBox="0 0 6 4"><path d="M0.5 0.5 L3 3 L5.5 0.5" fill="none" stroke="#555" stroke-width="0.8"/></svg></div>
<div class="select" style="left:548px;width:88px">Select Salary
  <svg width="6" height="4" viewBox="0 0 6 4"><path d="M0.5 0.5 L3 3 L5.5 0.5" fill="none" stroke="#555" stroke-width="0.8"/></svg></div>

<div class="jobs">
  <div class="jobs-head"><div>POSITION</div><div>SALARY</div><div>LOCATION</div><div>EXPERIENCE</div><div></div></div>

  <div class="job"><div><div class="job-title">Web Designer / Front End Developer</div><div class="job-company">Pixelgrain Solutions Private Limited</div><div class="job-posted">Posted : 9th Feb,2018</div></div><div>$2500-5000 P.A.</div><div>New York</div><div>2 - 6 yrs</div><div><span class="apply">APPLY JOB</span></div></div>
  <div class="job"><div><div class="job-title">Graphic &amp; Web Designer - Quick Hiring</div><div class="job-company">Thornmere Technologies Ltd.</div><div class="job-posted">Posted : 9th Feb,2018</div></div><div>$5200-8000 P.A.</div><div>Los Angeles</div><div>0 - 2 yrs</div><div><span class="apply">APPLY JOB</span></div></div>
  <div class="job"><div><div class="job-title">HTML / Web Designer / Front End Designer</div><div class="job-company">Vexa9 Webware Technologies Private Limited</div><div class="job-posted">Posted : 9th Feb,2018</div></div><div>$2500-5000 P.A.</div><div>England</div><div>2 - 6 yrs</div><div><span class="apply">APPLY JOB</span></div></div>
  <div class="job"><div><div class="job-title">SR. Graphic/ WEB- Designer</div><div class="job-company">Startup - AQUAFERN Pvt. Ltd.</div><div class="job-posted">Posted : 9th Feb,2018</div></div><div>$2500-5000 P.A.</div><div>New York</div><div>2 - 6 yrs</div><div><span class="apply">APPLY JOB</span></div></div>
  <div class="job"><div><div class="job-title">Account Manager</div><div class="job-company">Pixelgrain Solutions Private Limited</div><div class="job-posted">Posted : 9th Feb,2018</div></div><div>$2500-5000 P.A.</div><div>New York</div><div>2 - 6 yrs</div><div><span class="apply">APPLY JOB</span></div></div>
  <div class="job"><div><div class="job-title">Web Designer / Front End Developer</div><div class="job-company">Pixelgrain Solutions Private Limited</div><div class="job-posted">Posted : 9th Feb,2018</div></div><div>$2500-5000 P.A.</div><div>New York</div><div>2 - 6 yrs</div><div><span class="apply">APPLY JOB</span></div></div>
  <div class="job"><div><div class="job-title">Graphic &amp; Web Designer - Quick Hiring</div><div class="job-company">Thornmere Technologies Ltd.</div><div class="job-posted">Posted : 9th Feb,2018</div></div><div>$5200-8000 P.A.</div><div>Los Angeles</div><div>0 - 2 yrs</div><div><span class="apply">APPLY JOB</span></div></div>
  <div class="job"><div><div class="job-title">HTML / Web Designer / Front End Designer</div><div class="job-company">Vexa9 Webware Technologies Private Limited</div><div class="job-posted">Posted : 9th Feb,2018</div></div><div>$2500-5000 P.A.</div><div>England</div><div>2 - 6 yrs</div><div><span class="apply">APPLY JOB</span></div></div>
  <div class="job"><div><div class="job-title">SR. Graphic/ WEB- Designer</div><div class="job-company">Startup - AQUAFERN Pvt. Ltd.</div><div class="job-posted">Posted : 9th Feb,2018</div></div><div>$2500-5000 P.A.</div><div>New York</div><div>2 - 6 yrs</div><div><span class="apply">APPLY JOB</span></div></div>
  <div class="job"><div><div class="job-title">Account Manager</div><div class="job-company">Pixelgrain Solutions Private Limited</div><div class="job-posted">Posted : 9th Feb,2018</div></div><div>$2500-5000 P.A.</div><div>New York</div><div>2 - 6 yrs</div><div><span class="apply">APPLY JOB</span></div></div>
</div>

<div class="pager">
  <span class="arrow"><svg width="8" height="8" viewBox="0 0 8 8"><path d="M5 2 L3 4 L5 6 Z" fill="#fff"/></svg></span>
  <span>1</span><span>2</span><span>3</span><span>4</span><span>5</span>
  <span class="arrow"><svg width="8" height="8" viewBox="0 0 8 8"><path d="M3 2 L5 4 L3 6 Z" fill="#fff"/></svg></span>
</div>

<section class="newsletter">
  <h2>NEWSLETTER SUBSCRIBE</h2>
  <div class="field" style="left:23px">First Name</div>
  <div class="field" style="left:171px">Last Name</div>
  <div class="field" style="left:323px">E mail id</div>
  <div class="signup">SIGNUP</div>
</section>

<footer class="site-footer">
  <div class="foot-col" style="left:78px">
    <h3>INFORMATION</h3>
    <a>About Us</a><a>Terms &amp; Conditions</a><a>Privacy Policy</a><a>Careers with Us</a><a>Sitemap</a><a>Contact Us</a><a>FAQs</a>
  </div>
  <div class="foot-col" style="left:196px">
    <h3>BROWSE JOBS</h3>
    <a>Browse All Jobs</a><a>Premium MBA Jobs</a><a>Premium Engineering Jobs</a><a>Govt. Jobs</a><a>International Jobs</a><a>Jobs in Gulf</a><a>Jobs by Company</a>
  </div>
  <div class="foot-col" style="left:330px">
    <h3>EMPLOYERS</h3>
    <a>Post Jobs</a><a>Manage Responses</a><a>Report a Problem</a>
  </div>
  <div class="foot-col social" style="left:440px">
    <h3>FOLLOW US</h3>
    <a>Friendlane</a><a>Chirpline</a><a>Workmesh</a><a>Vantor Plus</a>
  </div>
  <div class="foot-brand">Veldmark</div>
  <div class="copyright">Copyrihgts @ 2018 All Rights Reserved</div>
</footer>

</body>
</html>
```